New Payments Start-up requires Logo, Style Guide and Web Site Design

We need a logo, style guide (colour templates etc.) and marketing web-site (HTML/CSS styling) for Kivex, a new account-to-account payment product for use in the Single European Payment Area (SEPA).

The design is for the product only, not a company brand. We're looking for basic palette and style guidelines also. The web site need only be a basic responsive cross-platform design and layout. We will produce our own content.

We have no requirements for specific colours or logo styles. It is a financial product, however, so should not appear too quirky or untrustworthy.

The product is still in the early phases of development, so we're not able to provide pictures or other content.

As a little more detail on how things work, though, our end customers will arrive at our site through redirection from our merchant partners (a number of whom are large multi-national companies) who have offered our services as an alternative to credit card payments. They will be able to set up a SEPA direct debit mandate online in just a few pages, secure that with a password and use it to pay both immediately and in future with a simple confirmation of the password… a quick, easy checkout.

Because we work with large customer in the payments space, whilst we’d like the brand to be modern and appealing, it has to engender trust and stability. Whilst this product is new and in start-up phase, our company has been in alternative payments for nearly 10 years and have strong products in Europe in the Pre-Paid Pelo/TrundlePay and Voucher space. We'd like to treat this separately, however, which is why we've briefed accordingly.

Project Deadline Extended
Reason: Apologies for the extension, but I had a couple of designers contact me to say they had completed work but were unable to submit because time ran out. I'll only extend this once, though, because we need to get cracking on the project. Many thanks Ben

Target Market(s)

European alternative payment customers

Industry/Entity Type

Financial

Logo Text

kivex

Coding

Coded - Design and coding required

Number of Pages Required

1 page

Font styles to use
Sans Serif

```html
<!DOCTYPE html>
<html lang="en">
<head>
<meta charset="utf-8">
<title>Kivex – Account-to-Account Payment</title>
<link rel="stylesheet" href="https://fonts.googleapis.com/css2?family=Open+Sans:wght@400;600;700&display=swap">
<style>
:root{
  --orange:#ff7e00;
  --orange-deep:#f06a00;
  --ink:#333333;
  --text:#777777;
  --light:#f4f4f4;
  --line:#e2e2e2;
  --footer-top:#585858;
  --footer-bottom:#343434;
  --white:#ffffff;
}
*{box-sizing:border-box;margin:0;padding:0}
html,body{width:1200px;height:2281px;overflow:hidden}
body{font-family:"Open Sans",Arial,sans-serif;color:var(--text);background:var(--white);position:relative}
.abs{position:absolute}
.btn{position:absolute;display:flex;align-items:center;justify-content:center;color:var(--white);font-weight:600;text-transform:uppercase;background:linear-gradient(var(--orange),var(--orange-deep));border-radius:2px}

/* header */
.site-header{position:absolute;left:0;top:0;width:1200px;height:91px;background:var(--white);border-top:4px solid var(--orange);box-shadow:0 1px 3px rgba(0,0,0,.08);z-index:2}
.logo{position:absolute;left:161px;top:29px;font-size:34px;font-weight:700;color:var(--orange);letter-spacing:1px;line-height:1}
.nav a{position:absolute;top:40px;font-size:12px;color:var(--ink);text-decoration:none;text-transform:uppercase;line-height:1}
.nav a.active{color:var(--orange)}
.nav-marker{position:absolute;left:488px;top:84px;width:0;height:0;border:7px solid transparent;border-bottom-color:var(--orange)}
.btn-login{left:910px;top:33px;width:57px;height:31px;font-size:11px}
.btn-signup{left:976px;top:33px;width:61px;height:31px;font-size:11px;background:#3c3c3c}

/* hero */
.hero{position:absolute;left:0;top:91px;width:1200px;height:461px;background:linear-gradient(90deg,#f3f3f3 0%,#f6f6f6 40%,#eef1f4 100%);overflow:hidden}
.hero-photo{position:absolute;left:500px;top:0;width:700px;height:461px;background:linear-gradient(100deg,rgba(246,246,246,0) 0%,#d9d4cf 30%,#c9b9ab 55%,#e8e6e4 100%)}
.hero-title{position:absolute;left:161px;top:118px;font-size:34px;line-height:43px;font-weight:600;color:var(--orange)}
.hero-title .dark{color:var(--ink)}
.hero-text{position:absolute;left:161px;top:222px;width:420px;font-size:14px;line-height:23px;color:#666}
.btn-hero{left:161px;top:298px;width:190px;height:37px;font-size:12px}
.slide-arrow{position:absolute;top:215px;width:32px;height:32px;border:1px solid #c8c8c8;border-radius:50%;display:flex;align-items:center;justify-content:center}

/* welcome */
.welcome{position:absolute;left:0;top:552px;width:1200px;height:364px;background:linear-gradient(110deg,var(--white) 0%,#fafafa 60%,#f1f1f1 100%);overflow:hidden}
.welcome-shade{position:absolute;left:0;top:0}
.welcome-art{position:absolute;left:175px;top:41px;width:335px;height:282px;background:radial-gradient(ellipse at 50% 45%,#5a8fbf 0%,#3a3a3a 45%,rgba(255,255,255,0) 72%)}
.section-title{font-size:23px;font-weight:600;text-transform:uppercase;color:var(--orange);line-height:1}
.section-title .dark{color:var(--ink)}
.welcome .section-title{position:absolute;left:625px;top:53px}
.lead{position:absolute;font-size:13px;line-height:23px;color:var(--orange)}
.body-copy{position:absolute;font-size:10.5px;line-height:19.5px;color:var(--text)}
.btn-small{font-size:10px;height:32px;width:96px}

/* how it works */
.how{position:absolute;left:0;top:916px;width:1200px;height:383px;background:var(--orange);color:var(--white)}
.how-title{position:absolute;left:0;width:1200px;top:40px;text-align:center;font-size:21px;font-weight:600;text-transform:uppercase}
.step{position:absolute;top:109px;width:220px;text-align:center}
.step-icon{width:98px;height:98px;margin:0 auto;border:4px solid var(--white);border-radius:50%;display:flex;align-items:center;justify-content:center}
.step-icon-inner{width:76px;height:76px;border-radius:50%;background:var(--white);display:flex;align-items:center;justify-content:center}
.step-name{margin-top:18px;font-size:13px;line-height:23px;font-weight:600;text-transform:uppercase}
.step-text{margin-top:16px;font-size:10.5px;line-height:19px}
.flow-arrow{position:absolute}

/* reasons */
.reasons{position:absolute;left:0;top:1299px;width:1200px;height:417px;background:var(--white)}
.reasons .section-title{position:absolute;left:0;width:1200px;top:38px;text-align:center}
.reason{position:absolute;top:93px;width:275px}
.reason-photo{width:275px;height:152px;border:1px solid var(--line);padding:3px;background:var(--white)}
.reason-photo div{width:100%;height:100%}
.reason-title{margin-top:12px;font-size:13.5px;color:var(--orange)}
.reason-text{margin-top:6px;font-size:10.5px;line-height:19.5px}
.read-more{margin-top:14px;font-size:10px;font-weight:600;color:var(--ink);text-transform:uppercase}

/* a2a */
.a2a{position:absolute;left:0;top:1716px;width:1200px;height:273px;background:#f7f7f7;overflow:hidden}
.card-tile{position:absolute;width:66px;height:37px;background:var(--white);border:1px solid #d6d6d6;box-shadow:1px 1px 2px rgba(0,0,0,.15);display:flex;align-items:center;justify-content:center;font-size:9px;font-weight:700;color:#2d4f8e}
.a2a .section-title{position:absolute;left:611px;top:44px}

/* footer */
.site-footer{position:absolute;left:0;top:1989px;width:1200px;height:232px;background:linear-gradient(var(--footer-top),var(--footer-bottom));color:var(--white)}
.footer-col{position:absolute;top:54px}
.footer-col h4{font-size:14px;font-weight:600;text-transform:uppercase;margin-bottom:10px}
.footer-col li{list-style:none;font-size:11px;line-height:23px}
.footer-col p{font-size:10.5px;line-height:16.5px}
.footer-more{margin-top:6px;font-size:10px;font-weight:600;text-transform:uppercase}
.email{position:absolute;left:797px;top:105px;width:240px;height:32px;background:var(--white);border:1px solid #ccc;border-radius:2px;font-size:10.5px;color:#555;padding:9px 12px}
.btn-subscribe{left:797px;top:150px;width:117px;height:37px;font-size:12px}
.bottom-bar{position:absolute;left:0;top:2221px;width:1200px;height:60px;background:var(--orange);color:var(--white)}
.copyright{position:absolute;left:161px;top:24px;font-size:10.5px}
.social{position:absolute;top:16px;width:28px;height:28px;border:1.5px solid var(--white);border-radius:50%}
</style>
</head>
<body>

<header class="site-header">
  <div class="logo">KIVEX</div>
  <nav class="nav">
    <a class="active" style="left:476px">Home</a>
    <a style="left:546px">About</a>
    <a style="left:620px">Send</a>
    <a style="left:686px">Business</a>
    <a style="left:773px">Sepa</a>
    <a style="left:836px">Contact</a>
  </nav>
  <div class="nav-marker"></div>
  <div class="btn btn-login">Login</div>
  <div class="btn btn-signup">Sign Up</div>
</header>

<section class="hero">
  <div class="hero-photo" role="img" aria-label="Couple smiling at a laptop while paying online with a card"></div>
  <h1 class="hero-title">New Account-to-Account<br><span class="dark">Payment</span> Product</h1>
  <p class="hero-text">Lorem ipsum dolor sit amet, consectetur adipiscing elit, sed do eiusmod tempor incididunt ut laborelorem ipmo.</p>
  <div class="btn btn-hero">Sign Up Now</div>
  <div class="slide-arrow" style="left:30px"><svg width="10" height="12" viewBox="0 0 10 12"><path d="M7 1 2 6l5 5" fill="none" stroke="#aaa" stroke-width="1.5"/></svg></div>
  <div class="slide-arrow" style="left:1140px"><svg width="10" height="12" viewBox="0 0 10 12"><path d="M3 1l5 5-5 5" fill="none" stroke="#aaa" stroke-width="1.5"/></svg></div>
</section>

<section class="welcome">
  <svg class="welcome-shade" width="1200" height="364"><polygon points="0,0 525,0 595,364 0,364" fill="#ffffff"/></svg>
  <div class="welcome-art" role="img" aria-label="Laptop with payment cards spilling from the screen and a mouse"></div>
  <h2 class="section-title">Welcome to <span class="dark">Kivex</span></h2>
  <p class="lead" style="left:625px;top:90px;width:420px">Lorem ipsum dolor sit amet, consectetur adipiscing elit, sed deiu sm tempor incididunt ut laborelorem ipmo.</p>
  <p class="body-copy" style="left:625px;top:153px;width:415px">Sed ut perspiciatis unde omnis iste natus error sit voluptatem accusantium dolore mq ue laudantium, totam rem aperiam, eaque ipsa quae ab illo inventore veritatis et quasi archit ecto beatae vitae dicta sunt explicabo. Nemo enim ipsam volupta tem quia volup tas sit aspernatur aut odit aut fugit, sed quia conse quun tur mag ni dolores eos qui rati one voluptatem sequi nesciunt.</p>
  <div class="btn btn-small" style="left:625px;top:274px">Read More »</div>
</section>

<section class="how">
  <h2 class="how-title">How does it work?</h2>
  <svg class="flow-arrow" style="left:318px;top:118px" width="100" height="40" viewBox="0 0 100 40"><path d="M5 30 Q45 0 85 18" fill="none" stroke="#ffa14a" stroke-width="8" stroke-linecap="round"/><path d="M80 6 96 22 76 28Z" fill="#ffa14a"/></svg>
  <svg class="flow-arrow" style="left:568px;top:138px" width="100" height="40" viewBox="0 0 100 40"><path d="M5 22 Q45 40 85 14" fill="none" stroke="#ffa14a" stroke-width="8" stroke-linecap="round"/><path d="M74 4 96 8 86 28Z" fill="#ffa14a"/></svg>
  <svg class="flow-arrow" style="left:788px;top:118px" width="100" height="40" viewBox="0 0 100 40"><path d="M5 30 Q45 0 85 18" fill="none" stroke="#ffa14a" stroke-width="8" stroke-linecap="round"/><path d="M80 6 96 22 76 28Z" fill="#ffa14a"/></svg>

  <div class="step" style="left:139px">
    <div class="step-icon"><div class="step-icon-inner"><svg width="34" height="34" viewBox="0 0 34 34"><circle cx="17" cy="10" r="7" fill="#ff7e00"/><path d="M3 33c0-9 6-13 14-13s14 4 14 13Z" fill="#ff7e00"/><path d="M15 20h4l-1 9h-2Z" fill="#fff"/></svg></div></div>
    <div class="step-name">Our End<br>Customers</div>
    <p class="step-text">Sed ut perspiciatis unde otsrs itvoluptatem accusan tium dolore mq ue laudpta te iu dololorlo</p>
  </div>
  <div class="step" style="left:374px">
    <div class="step-icon"><div class="step-icon-inner"><svg width="38" height="32" viewBox="0 0 38 32"><ellipse cx="18" cy="18" rx="15" ry="11" fill="#ff7e00"/><rect x="8" y="25" width="5" height="6" fill="#ff7e00"/><rect x="23" y="25" width="5" height="6" fill="#ff7e00"/><path d="M32 15l5-2v6l-5-1Z" fill="#ff7e00"/><circle cx="18" cy="6" r="5" fill="#ff7e00"/><rect x="14" y="11" width="8" height="2" fill="#fff"/></svg></div></div>
    <div class="step-name">Merchant<br>Partners</div>
    <p class="step-text">Sed ut perspiciatis unde otsrs itvoluptatem accusan tium dolore mq ue laudpta te iu dololorlo</p>
  </div>
  <div class="step" style="left:609px">
    <div class="step-icon"><div class="step-icon-inner"><svg width="40" height="30" viewBox="0 0 40 30"><rect x="8" y="2" width="30" height="20" rx="2" fill="#ffb066"/><rect x="2" y="8" width="30" height="20" rx="2" fill="#ff7e00"/><rect x="2" y="12" width="30" height="4" fill="#fff"/><rect x="6" y="21" width="10" height="3" fill="#fff"/></svg></div></div>
    <div class="step-name">Credit<br>Card Network</div>
    <p class="step-text">Sed ut perspiciatis unde otsrs itvoluptatem accusan tium dolore mq ue laudpta te iu dololorlo</p>
  </div>
  <div class="step" style="left:844px">
    <div class="step-icon"><div class="step-icon-inner"><svg width="30" height="34" viewBox="0 0 30 34"><path d="M8 15V10a7 7 0 0 1 14 0v5" fill="none" stroke="#ff7e00" stroke-width="4"/><rect x="3" y="15" width="24" height="18" rx="2" fill="#ff7e00"/></svg></div></div>
    <div class="step-name">Quick,<br>Easy Checkout</div>
    <p class="step-text">Sed ut perspiciatis unde otsrs itvoluptatem accusan tium dolore mq ue laudpta te iu dololorlo</p>
  </div>
</section>

<section class="reasons">
  <h2 class="section-title">More reasons to use <span class="dark">Kivex</span></h2>
  <article class="reason" style="left:160px">
    <div class="reason-photo"><div role="img" aria-label="Hands typing on a laptop keyboard" style="background:linear-gradient(120deg,#d9dfe6,#9fa6ae 55%,#c9a18c)"></div></div>
    <h3 class="reason-title">Lorem ipsum dolor sit amet, conse</h3>
    <p class="reason-text">Sed ut p loerspiciatis unde omnis iste natus error sit volup tatem accusantium dolore mq uloe laud antium, tota m rem aperiam, eaque ipsa quae ab.</p>
    <div class="read-more">Read More »</div>
  </article>
  <article class="reason" style="left:462px">
    <div class="reason-photo"><div role="img" aria-label="Person holding a smartphone showing a payment confirmation" style="background:linear-gradient(100deg,#3b3633,#8a7a70 50%,#d8d4d0)"></div></div>
    <h3 class="reason-title">Lorem ipsum dolor sit amet, conse</h3>
    <p class="reason-text">Sed ut p loerspiciatis unde omnis iste natus error sit volup tatem accusantium dolore mq uloe laud antium, tota m rem aperiam, eaque ipsa quae ab.</p>
    <div class="read-more">Read More »</div>
  </article>
  <article class="reason" style="left:765px">
    <div class="reason-photo"><div role="img" aria-label="Two phones exchanging a contactless payment" style="background:linear-gradient(100deg,#c98a8a,#4a4f55 50%,#e6a8b4)"></div></div>
    <h3 class="reason-title">Lorem ipsum dolor sit amet, conse</h3>
    <p class="reason-text">Sed ut p loerspiciatis unde omnis iste natus error sit volup tatem accusantium dolore mq uloe laud antium, tota m rem aperiam, eaque ipsa quae ab.</p>
    <div class="read-more">Read More »</div>
  </article>
</section>

<section class="a2a">
  <svg class="abs" style="left:0;top:0" width="1200" height="273"><polygon points="585,0 1200,0 1200,273 505,273" fill="#ffffff"/></svg>
  <div class="card-tile" style="left:182px;top:53px">Pelo</div>
  <div class="card-tile" style="left:256px;top:53px;font-size:7.5px">TrundlePay</div>
  <div class="card-tile" style="left:331px;top:53px;font-size:8px">Amberline</div>
  <div class="card-tile" style="left:401px;top:53px">Farpoint</div>
  <div class="card-tile" style="left:175px;top:99px">Tilo</div>
  <div class="card-tile" style="left:248px;top:99px">Vyra</div>
  <div class="card-tile" style="left:324px;top:99px">Dinvale</div>
  <div class="card-tile" style="left:396px;top:99px">Brisko</div>
  <div class="card-tile" style="left:166px;top:146px">Northway</div>
  <div class="card-tile" style="left:240px;top:146px">Coinlane</div>
  <div class="card-tile" style="left:314px;top:146px">Cheqo</div>
  <div class="card-tile" style="left:390px;top:146px">Jarro</div>
  <div class="card-tile" style="left:160px;top:193px">Mesto</div>
  <div class="card-tile" style="left:232px;top:193px">Stratio</div>
  <div class="card-tile" style="left:307px;top:193px">Unova</div>
  <h2 class="section-title">Account-to-account <span class="dark">Payment</span></h2>
  <p class="body-copy" style="left:611px;top:89px;width:430px">Sed ut perspiciatis unde omnis iste natus error sit voluptatem accusantium dolore mq ue laudantium, totam rem aperiam, eaque ipsa quae ab illo inventore veritatis et quasi archit ecto beatae vitae dicta sunt explicabo. Nemo enim ipsam volupta tem quia volup tas sit aspernatur aut odit aut fugit, sed quia conse quun tur mag ni dolores eos qui rati one voluptatem sequi nesciunt.</p>
  <div class="btn btn-small" style="left:614px;top:205px">Read More »</div>
</section>

<footer class="site-footer">
  <div class="footer-col" style="left:161px;width:190px">
    <h4>Kivex</h4>
    <p>Sed ut perspiciatis unde omnis isten error sit voluptatem accusantiloudo emq ue laudantiu totavoluptatcusa ntiloum dolor emq ue lauda.</p>
    <div class="footer-more">Read more about SEPA</div>
  </div>
  <div class="footer-col" style="left:427px">
    <h4>Resources</h4>
    <ul><li>Support</li><li>Security Center</li><li>Developer Center</li><li>Shopping Carts</li><li>Legal</li></ul>
  </div>
  <div class="footer-col" style="left:611px">
    <h4>Support</h4>
    <ul><li>FAQs</li><li>Privacy Policy</li><li>Recommendations</li><li>Contact</li></ul>
  </div>
  <div class="footer-col" style="left:794px">
    <h4>Sign up newsletter</h4>
    <p style="font-size:11px;margin-top:-4px">Please sign up here for latest deals</p>
  </div>
  <div class="email">Email address</div>
  <div class="btn btn-subscribe">Subscribe</div>
</footer>

<div class="bottom-bar">
  <div class="copyright">© 2016 Kivex.&nbsp; All copyrights are reserved&nbsp; Term of Use</div>
  <div class="social" style="left:876px"></div>
  <div class="social" style="left:909px"></div>
  <div class="social" style="left:943px"></div>
  <div class="social" style="left:976px"></div>
  <div class="social" style="left:1010px"></div>
</div>

</body>
</html>
```